Biz Card Design TPVC

New business card for a new company.
Logo was completed by a designer on ArtFlock and looking to continue requesting additional services.
Company Name: Tidal Prime Voltage Collective
Although this company is starting in Canada, we will be moving towards a global presence within the next 6 months.
Key elements to this business are as follows.
Energy Procurement
Energy Reduction Services
Demand Side Consulting
Energy Efficiency Consulting
Saving Clients Money
Helping Them Go "Green"
Managing Their Energy Requirements
Basically the goal for our company is to find the best procurement solution for our clients and reduce their energy consumption. This reduces their expenses and the amount of greenhouse gas they produce on a daily basis.
I have been in the energy footprint for the last 20 years and know that most companies are looking to "do whatever is necessary to get them to sign on the dotted line". I would prefer to walk away from a client that I can't help than to put them into a situation that they will regret for years to come. This is where the "TIDAL" part of the company name comes from.
The following is a catch phrase that encompasses what we do.
"Reducing your carbon footprint & energy bill at the same time!"
The back of the card needs to have this statement along with some sort of illustration. The back is a playground for creative ideas.
The front of the card needs the following.
Logo.
First & Last Name (Gus Marwick)
Title (Energy Warrior)
Phone Number (555) 314-2768
Fax Number (555) 862-4091
Email Address gus@tidalprimevoltage.example
Address 47 Orchard Lane Toronto Ontario K4P 2Z7
I want it to be a card that is remembered when any of my staff give it to a customer. It HAS to stand out.
Target Market(s)
Business Owners, Decision Makers, 30 to 65+
Industry/Entity Type
Business
Look and feel
Each slider illustrates characteristics of the customer's brand and the style your logo design should communicate.

```html
<!DOCTYPE html>
<html lang="en">
<head>
<meta charset="utf-8">
<title>Tidal Prime Voltage Collective – Business Card</title>
<link rel="stylesheet" href="https://fonts.googleapis.com/css2?family=Cinzel:wght@400;500&display=swap">
<style>
  :root {
    --card-dark: #2c2c2e;
    --card-dark-edge: #1d1d1f;
    --card-dark-glow: #4a4a4d;
    --card-light: #d6d6d6;
    --card-light-edge: #c4c4c4;
    --text-light: #f2f2f2;
    --text-dark: #1f1f1f;
    --brand-green: #6dbb4e;
    --brand-blue: #3b6fb6;
    --brand-faint: #8ea7c2;
    --brand-faint-green: #a9d3a4;
  }
  * { margin: 0; padding: 0; box-sizing: border-box; }
  html, body { width: 994px; height: 1200px; overflow: hidden; }
  body {
    position: relative;
    font-family: "Cinzel", serif;
    background: var(--card-light);
  }
  .card-front {
    position: absolute; left: 0; top: 0; width: 994px; height: 629px;
    color: var(--text-light);
  }
  .front-texture {
    position: absolute; inset: 0;
    background: radial-gradient(ellipse at 55% 40%, var(--card-dark-glow) 0%, var(--card-dark) 45%, var(--card-dark-edge) 100%);
  }
  .brand-mark {
    position: absolute; left: 66px; top: 36px; width: 424px; text-align: center;
  }
  .brand-dot {
    display: block; width: 58px; height: 58px; border-radius: 50%;
    background: var(--brand-green); margin: 0 auto 14px;
  }
  .brand-name {
    font-size: 19px; font-weight: 500; color: var(--brand-blue); letter-spacing: .5px; white-space: nowrap;
  }
  .service-list { position: absolute; left: 594px; top: 152px; list-style: none; }
  .service-list li {
    display: flex; align-items: center; height: 45px;
    font-size: 15px; letter-spacing: 1.2px;
  }
  .service-bullet {
    width: 22px; height: 22px; border-radius: 50%; background: var(--brand-green);
    margin-right: 30px; flex: none;
  }
  .contact { position: absolute; left: 66px; top: 364px; }
  .contact-name { font-size: 30px; font-weight: 500; letter-spacing: 1.5px; line-height: 1; }
  .contact-title { font-size: 13px; letter-spacing: 1px; margin-top: 10px; margin-bottom: 14px; }
  .contact-line { font-size: 17px; letter-spacing: 1.5px; line-height: 35px; white-space: nowrap; }

  .card-back {
    position: absolute; left: 0; top: 629px; width: 994px; height: 571px;
    background: radial-gradient(ellipse at 50% 40%, var(--card-light) 0%, var(--card-light-edge) 100%);
    text-align: center; color: var(--text-dark);
  }
  .tagline {
    position: absolute; left: 0; right: 0; top: 74px;
    font-size: 32px; letter-spacing: 3px; line-height: 61px;
  }
  .back-dot {
    position: absolute; left: 427px; top: 270px; width: 140px; height: 140px; border-radius: 50%;
    background: var(--brand-faint-green); opacity: .8;
  }
  .back-brand-name {
    position: absolute; left: 0; right: 0; top: 440px;
    font-size: 38px; font-weight: 500; color: var(--brand-faint); white-space: nowrap;
  }
</style>
</head>
<body>
  <section class="card-front">
    <div class="front-texture" role="img" aria-label="Dark woven plaid background texture"></div>
    <div class="brand-mark">
      <span class="brand-dot"></span>
      <div class="brand-name">Tidal Prime Voltage Collective</div>
    </div>
    <ul class="service-list">
      <li><span class="service-bullet"></span>Energy Procurement</li>
      <li><span class="service-bullet"></span>Energy Reduction Services</li>
      <li><span class="service-bullet"></span>Demand Side Consulting</li>
      <li><span class="service-bullet"></span>Energy Efficiency Consulting</li>
    </ul>
    <div class="contact">
      <div class="contact-name">Gus Marwick</div>
      <div class="contact-title">(Energy Warrior)</div>
      <div class="contact-line">Phone: (555) 314-2768</div>
      <div class="contact-line">Fax: (555) 862-4091</div>
      <div class="contact-line">Email: gus@tidalprimevoltage.example</div>
      <div class="contact-line">Address: 47 Orchard Lane Toronto Ontario K4P 2Z7</div>
    </div>
  </section>

  <section class="card-back">
    <p class="tagline">"Reducing your carbon footprint<br>&amp;<br>energy bill at the same time!"</p>
    <span class="back-dot"></span>
    <div class="back-brand-name">Tidal Prime Voltage Collective</div>
  </section>
</body>
</html>
```